Events & Entertainment Production Coordination Business Cards

We need a business card for a new company based in Los Angeles called "Bright Stage Works"
Our company brings people together for events and helps coordinate different productions. We bring artists from a different country to perform or do events in the U.S.
We are looking for something fun, lively, colorful, creative, and simple.
Nothing that looks too crisp, dark, stiff, or modern.
We connect people from different parts of the world, so definitely something eye-catching will be great!
Colors we would like to see are Black, Yellow, Red, White, Brown to name a few. (Feel free to use more!)
(Double-sided is an option also)
Industry/Entity Type
Business
Contact Information for Business Card
Contact Information to put on Business Card:
Name
Title
Address - 2 lines
Phone - place for 3 numbers
E-mail
URL
Look and feel

```html
<!DOCTYPE html>
<html lang="en">
<head>
<meta charset="utf-8">
<title>Bright Stage Works – Business Card</title>
<link rel="stylesheet" href="https://fonts.googleapis.com/css2?family=Lato:wght@400;700;900&display=swap">
<style>
  :root {
    --stage: #2e2e2e;
    --brand-red: #b80d12;
    --brand-red-deep: #8f0a0e;
    --ink: #2a2a2a;
    --paper: #f7f7f7;
    --paper-edge: #e6e6e6;
    --map-tint: #f1d9da;
  }
  * { box-sizing: border-box; margin: 0; padding: 0; }
  html, body {
    width: 1200px; height: 997px; overflow: hidden;
    background: var(--stage);
    font-family: "Lato", sans-serif;
  }
  .canvas { position: relative; width: 1200px; height: 997px; }

  .card {
    position: absolute; width: 580px; height: 331px;
    border-radius: 3px;
    box-shadow: 0 18px 40px rgba(0,0,0,.45);
    overflow: hidden;
  }

  /* Front side */
  .card--front {
    left: 80px; top: 130px;
    background: radial-gradient(ellipse at 40% 40%, #cc1217 0%, var(--brand-red) 55%, var(--brand-red-deep) 100%);
  }
  .card--front .world-map {
    position: absolute; left: 150px; top: 70px; width: 380px; height: 200px;
    background: radial-gradient(ellipse at center, rgba(120,0,4,.35), rgba(120,0,4,0) 70%);
  }
  .card--front .brand-name {
    position: absolute; left: 0; right: 0; top: 145px;
    text-align: center;
    font-weight: 900; font-size: 34px; letter-spacing: 3px;
    text-transform: uppercase; color: #ffffff;
  }

  /* Back side */
  .card--back {
    left: 540px; top: 520px;
    background: linear-gradient(135deg, #ffffff 0%, var(--paper) 60%, var(--paper-edge) 100%);
  }
  .card--back .world-map {
    position: absolute; left: 120px; top: 60px; width: 400px; height: 230px;
    background: radial-gradient(ellipse at center, var(--map-tint) 0%, rgba(241,217,218,0) 70%);
  }
  .card--back .brand-name {
    position: absolute; left: 0; right: 0; top: 42px;
    text-align: center;
    font-weight: 900; font-size: 26px; letter-spacing: 2px;
    text-transform: uppercase; color: var(--brand-red);
  }

  .identity {
    position: absolute; left: 40px; top: 145px; width: 230px; text-align: right;
  }
  .identity .person-name { font-weight: 700; font-size: 20px; color: var(--brand-red); }
  .identity .person-title { font-size: 15px; color: var(--ink); margin-top: 2px; }
  .identity .address {
    margin-top: 34px; font-weight: 700; font-size: 16px; line-height: 1.35; color: var(--brand-red);
  }

  .divider {
    position: absolute; left: 292px; top: 138px; width: 3px; height: 120px;
    background: linear-gradient(to bottom, rgba(184,13,18,0), var(--brand-red) 30%, var(--brand-red) 60%, rgba(184,13,18,0));
  }

  .contact-list {
    position: absolute; left: 318px; top: 130px; list-style: none;
  }
  .contact-list li {
    display: flex; align-items: center; gap: 10px;
    font-size: 15px; color: var(--ink); height: 27px;
  }
  .contact-list svg { width: 16px; height: 16px; fill: var(--brand-red-deep); flex: none; }
</style>
</head>
<body>
<main class="canvas">

  <section class="card card--front" aria-label="Card front">
    <div class="world-map" role="img" aria-label="Faint dotted world map in deep red"></div>
    <p class="brand-name">Bright Stage Works</p>
  </section>

  <section class="card card--back" aria-label="Card back">
    <div class="world-map" role="img" aria-label="Light pink dotted world map"></div>
    <p class="brand-name">Bright Stage Works</p>

    <div class="identity">
      <p class="person-name">Daniel Reyes</p>
      <p class="person-title">Chief Operating Officer</p>
      <p class="address">48 Harlow Avenue,<br>Fairview, CA 90012</p>
    </div>

    <div class="divider"></div>

    <ul class="contact-list">
      <li>
        <svg viewBox="0 0 16 16" aria-hidden="true"><path d="M2 5c0-2 2-3 6-3s6 1 6 3v1h-3V5H5v1H2zM4 7h8l2 6H2zm4 1.5a2 2 0 1 0 0 4 2 2 0 0 0 0-4z"/></svg>
        310-555-0142
      </li>
      <li>
        <svg viewBox="0 0 16 16" aria-hidden="true"><path d="M4 1h8v4H4zM1 6h14v6h-3v3H4v-3H1zm4 5v3h6v-3z"/></svg>
        310-555-0148
      </li>
      <li>
        <svg viewBox="0 0 16 16" aria-hidden="true"><path d="M1 3h14v10H1zm1.5 1.5L8 9l5.5-4.5z"/></svg>
        dan@brightstageworks.com
      </li>
      <li>
        <svg viewBox="0 0 16 16" aria-hidden="true"><path d="M6.5 9.5l3-3 1 1-3 3zM5 8l-2 2a2 2 0 0 0 3 3l2-2 1 1-2 2a3.5 3.5 0 0 1-5-5l2-2zm6 0l2-2a2 2 0 0 0-3-3L8 5 7 4l2-2a3.5 3.5 0 0 1 5 5l-2 2z"/></svg>
        www.brightstageworks.com
      </li>
    </ul>
  </section>

</main>
</body>
</html>
```